Digital ad to Parent Funnel

Little Comet Lab works with preschoolers (also ages 2-8) doing hands-on activities that are Science Tech Engineering and Math (STEM) as a service business. The design is subtly colorful with the attached swatch definitions. Hexagons are a theme on the website.
www.littlecometlab.com
The purpose is on social media with a call to action to a landing page. I'd like placeholder text so I can be the copywriter. The banner I see is vertical, longer than wider. Design elements are welcoming, cheerful, and concrete. Pictures included are thematic for reference
https://www.pinterest.com/cometlabKT/website-mood-board/
I'd like fonts that are more used than Dosis, which has a child-like font but doesn't render well online. Versatile design desired for deferring ad sizes, if possible. My laptop has InDesign.
Thanks!

```html
<!DOCTYPE html>
<html lang="en">
<head>
<meta charset="utf-8">
<title>Little Comet Lab – Parent Ad</title>
<link rel="stylesheet" href="https://fonts.googleapis.com/css2?family=Dosis:wght@600;700;800&family=Open+Sans:wght@400;600;700&display=swap">
<style>
  :root {
    --stage: #d8dbde;
    --card-top: #f3f3f3;
    --card-bottom: #e4e4e4;
    --purple: #6a2c90;
    --ink: #454545;
    --price-ink: #4a4a4a;
    --sky: #36a5de;
    --sky-edge: #1f87c2;
    --white: #ffffff;
  }
  * { margin: 0; padding: 0; box-sizing: border-box; }
  html, body {
    width: 1200px; height: 1200px; overflow: hidden;
    background: var(--stage);
  }
  .ad {
    position: absolute; left: 285px; top: 40px;
    width: 630px; height: 1120px; overflow: hidden;
    background: linear-gradient(180deg, var(--card-top) 0%, var(--card-bottom) 100%);
  }
  .ad__art { position: absolute; inset: 0; width: 100%; height: 100%; }
  .ad__copy { position: absolute; left: 52px; top: 48px; width: 540px; }
  .headline {
    font-family: "Dosis", sans-serif; font-weight: 800;
    font-size: 52px; line-height: 56px; color: var(--purple);
  }
  .body-text {
    margin-top: 8px;
    font-family: "Open Sans", sans-serif; font-weight: 400;
    font-size: 21px; line-height: 30px; color: var(--ink);
  }
  .price {
    margin-top: 22px;
    font-family: "Dosis", sans-serif; font-weight: 800;
    font-size: 29px; line-height: 34px; color: var(--price-ink);
  }
  .price__amount { font-size: 36px; }
  .more-link {
    margin-top: 6px;
    font-family: "Open Sans", sans-serif; font-weight: 400;
    font-size: 21px; line-height: 28px; color: var(--purple);
  }
  .brand {
    position: absolute; left: 52px; top: 510px;
    display: flex; align-items: center; gap: 14px;
  }
  .brand__dot {
    width: 44px; height: 44px; border-radius: 50%; background: var(--purple);
  }
  .brand__name {
    font-family: "Dosis", sans-serif; font-weight: 800;
    font-size: 36px; color: var(--purple);
  }
  .cta {
    position: absolute; left: 34px; top: 1033px;
    width: 244px; height: 54px; border-radius: 27px;
    background: var(--sky); border: 2px solid var(--sky-edge);
    display: flex; align-items: center; justify-content: center;
    font-family: "Open Sans", sans-serif; font-weight: 700;
    font-size: 31px; color: var(--white); letter-spacing: 0.5px;
  }
</style>
</head>
<body>
  <main class="ad">
    <svg class="ad__art" viewBox="0 0 500 890" preserveAspectRatio="none" aria-hidden="false">
      <defs>
        <linearGradient id="photo-tone" x1="0" y1="0" x2="0.6" y2="1">
          <stop offset="0" stop-color="#f1eef2"/>
          <stop offset="0.45" stop-color="#e3c9dc"/>
          <stop offset="0.75" stop-color="#b892b0"/>
          <stop offset="1" stop-color="#232842"/>
        </linearGradient>
      </defs>
      <path class="curl-shadow" d="M56,604 C200,512 330,430 452,418 L500,420 L500,432 L450,427 C330,442 200,522 60,612 Z" fill="#ffffff"/>
      <path class="photo-area" role="img" aria-label="Photo: smiling child holding up a spinning rainbow pinwheel"
            d="M60,610 C200,520 330,440 450,427 L500,432 L500,890 L298,890 C250,780 160,680 60,650 Z"
            fill="url(#photo-tone)"/>
      <path class="curl-band" d="M60,650 C160,680 250,780 298,890 L282,890 C225,790 150,705 58,668 Z" fill="#6a2c90"/>
    </svg>

    <section class="ad__copy">
      <h1 class="headline">Children matter,<br>how about you?</h1>
      <p class="body-text">As a Maker of Experiences, Little Comet Lab brings you relief. She increases the potential and joy in your children with STEM activities. Playgroups or Mother's Helper.</p>
      <p class="price">One hour is <span class="price__amount">$8</span> per 2-8 yo</p>
      <p class="more-link">More...at littlecometlab.com/at-home-mom</p>
    </section>

    <div class="brand">
      <span class="brand__dot"></span>
      <span class="brand__name">Little Comet Lab</span>
    </div>

    <div class="cta">Message</div>
  </main>
</body>
</html>
```